Vantage Sport And Fitness- Rates

I am opening up a new Gym/Training Facility. The Name of my New gym is Vantage Sports And Fitness. I am wanting to design a card that captures Membership Pricing/Personal Training Pricing. I will Upload the Logo. My colors are Red/Black/Silver. I really want there pricing card to "POP". IT needs to be very Professional and Clean. I will be placing these cards on a 5'7 . I would like these item on the card:
Name of Company: Vantage Sports And Fitness
Address:
2817 Larkmoor Commerce Dr.
Suite 214 Chantilly, VA 20153
Phone #: 703-555-0187
website: www.vantagesnf-example.com
Membership Rates:
$99/Month
$49 Heroes Rate
Family Plan:
2 People $149
3 People $199
4 People $299
Personal Training Rates:
1 session $102
5 sessions $490
10 sessions $940
20 sessions $1,800
40 sessions $3,400
Please be creative

```html
<!DOCTYPE html>
<html lang="en">
<head>
<meta charset="utf-8">
<title>Vantage Sports And Fitness – Rates</title>
<link rel="stylesheet" href="https://fonts.googleapis.com/css2?family=Oswald:wght@300;400;500&family=Open+Sans:wght@400;600&display=swap">
<style>
  :root {
    --red: #e81e25;
    --charcoal: #333333;
    --footer: #3c3c3c;
    --silver-light: #d8d8d8;
    --silver-mid: #9a9a9a;
    --silver-dark: #5e5e5e;
    --stage: #8a8a8a;
    --white: #ffffff;
  }
  * { margin: 0; padding: 0; box-sizing: border-box; }
  html, body { width: 1200px; height: 1200px; overflow: hidden; background: var(--stage); }
  .rate-card {
    position: absolute; left: 198px; top: 40px;
    width: 804px; height: 1120px; overflow: hidden;
    background: var(--silver-mid);
    box-shadow: 0 4px 18px rgba(0,0,0,.25);
  }
  .hero-photo {
    position: absolute; left: 0; top: 0; width: 804px; height: 993px;
    background:
      linear-gradient(90deg, rgba(0,0,0,0) 60%, rgba(150,105,80,.55) 75%, rgba(70,55,50,.7) 100%),
      radial-gradient(ellipse at 40% 10%, var(--silver-light) 0%, var(--silver-mid) 55%, var(--silver-dark) 100%);
  }
  .brand-name {
    position: absolute; left: 61px; top: 50px;
    font-family: 'Oswald', sans-serif; font-weight: 400; color: var(--charcoal);
    font-size: 34px; line-height: 1.2;
  }
  .label-bar {
    position: absolute; left: 61px; top: 158px; width: 327px; height: 48px;
    background: var(--red); color: var(--white);
    font-family: 'Oswald', sans-serif; font-weight: 300; font-size: 38px; line-height: 48px; padding-left: 16px;
  }
  .headline-price {
    position: absolute; left: 76px;
    font-family: 'Oswald', sans-serif; font-weight: 500; color: var(--red); font-size: 56px; line-height: 1; letter-spacing: -.5px;
  }
  .price-month { top: 228px; }
  .price-heroes { top: 302px; }
  .rate-table { position: absolute; left: 61px; width: 330px; }
  .rate-table__head {
    background: var(--charcoal); color: var(--white); text-align: center;
    font-family: 'Oswald', sans-serif; font-weight: 400; font-size: 32px; line-height: 40px; letter-spacing: -.5px;
  }
  .rate-table__body { background: var(--red); padding: 8px 0; }
  .rate-row {
    display: flex; font-family: 'Open Sans', sans-serif; font-weight: 600; color: var(--white);
    font-size: 24px; height: 41.5px; align-items: center;
  }
  .family-plan { top: 385px; }
  .family-plan .rate-row span:first-child { width: 195px; padding-left: 46px; }
  .training { top: 600px; }
  .training .rate-table__body { padding: 2px 0 10px; }
  .training .rate-row span:first-child { width: 209px; padding-left: 36px; }
  .contact-bar {
    position: absolute; left: 0; top: 993px; width: 804px; height: 127px;
    background: var(--footer); color: var(--white);
    font-family: 'Open Sans', sans-serif; font-size: 17px;
  }
  .contact-item { position: absolute; display: flex; align-items: flex-start; line-height: 24px; white-space: nowrap; }
  .contact-item svg { flex: none; margin-right: 5px; margin-top: 5px; }
  .contact-address { left: 16px; top: 24px; }
  .contact-phone { left: 346px; top: 32px; font-size: 19px; }
  .contact-web { left: 556px; top: 32px; font-size: 15px; }
  .divider { position: absolute; top: 27px; width: 2px; height: 50px; background: var(--white); }
</style>
</head>
<body>
<main class="rate-card">
  <div class="hero-photo" role="img" aria-label="Greyscale gym interior with a fit athlete in a sports top holding a red dumbbell"></div>

  <header class="brand-name">Vantage Sports And Fitness</header>

  <div class="label-bar">Membership Rates:</div>
  <div class="headline-price price-month">$99/Month</div>
  <div class="headline-price price-heroes">$49 Heroes Rate</div>

  <section class="rate-table family-plan">
    <h2 class="rate-table__head">Family Plan:</h2>
    <div class="rate-table__body">
      <div class="rate-row"><span>2 People</span><span>$149</span></div>
      <div class="rate-row"><span>3 People</span><span>$199</span></div>
      <div class="rate-row"><span>4 People</span><span>$299</span></div>
    </div>
  </section>

  <section class="rate-table training">
    <h2 class="rate-table__head">Personal Training Rates:</h2>
    <div class="rate-table__body">
      <div class="rate-row"><span>1 session</span><span>$102</span></div>
      <div class="rate-row"><span>5 sessions</span><span>$490</span></div>
      <div class="rate-row"><span>10 sessions</span><span>$940</span></div>
      <div class="rate-row"><span>20 sessions</span><span>$1800</span></div>
      <div class="rate-row"><span>40 sessions</span><span>$3400</span></div>
    </div>
  </section>

  <footer class="contact-bar">
    <div class="contact-item contact-address">
      <svg width="11" height="15" viewBox="0 0 11 15"><path d="M5.5 0A5.5 5.5 0 0 0 0 5.5C0 9.5 5.5 15 5.5 15S11 9.5 11 5.5A5.5 5.5 0 0 0 5.5 0Zm0 7.7a2.2 2.2 0 1 1 0-4.4 2.2 2.2 0 0 1 0 4.4Z" fill="#fff"/></svg>
      <div>2817 Larkmoor Commerce Dr.<br>Suite 214 Chantilly, VA 20153</div>
    </div>
    <div class="divider" style="left:317px"></div>
    <div class="contact-item contact-phone">
      <svg width="15" height="15" viewBox="0 0 24 24"><path d="M6.6 10.8a15 15 0 0 0 6.6 6.6l2.2-2.2a1 1 0 0 1 1-.25 11.4 11.4 0 0 0 3.6.57 1 1 0 0 1 1 1V20a1 1 0 0 1-1 1A17 17 0 0 1 3 4a1 1 0 0 1 1-1h3.5a1 1 0 0 1 1 1c0 1.25.2 2.45.57 3.57a1 1 0 0 1-.25 1Z" fill="#fff"/></svg>
      <span>703-555-0187</span>
    </div>
    <div class="divider" style="left:537px"></div>
    <div class="contact-item contact-web">
      <svg width="15" height="15" viewBox="0 0 16 16"><circle cx="8" cy="8" r="7" fill="none" stroke="#fff" stroke-width="1.6"/><path d="M1 8h14M8 1c2.5 2.5 2.5 11.5 0 14M8 1c-2.5 2.5-2.5 11.5 0 14" fill="none" stroke="#fff" stroke-width="1.2"/></svg>
      <span>www.vantagesnf-example.com</span>
    </div>
  </footer>
</main>
</body>
</html>
```